B2B Tear Sheet / Flyer for Corvana Summit Partners

Design multiple creative treatments for a 1-page, 2-sided tear sheet/flyer for a B2B consulting firm called Corvana Summit Partners, targeting Private Equity firms, Family Offices, Investment Banks, and Independent Sponsors. This piece will be handed out at conferences, 1-on-1 meetings, and potential snail mail (direct mail) campaigns. Eventually, the piece could also be made available on our website. The company is in start-up mode, so our website is not yet up and working. But we do have a logo and color palette.

```html
<!DOCTYPE html>
<html lang="en">
<head>
<meta charset="utf-8">
<title>Corvana Summit Partners – Tear Sheet</title>
<link href="https://fonts.googleapis.com/css2?family=PT+Serif:wght@400;700&family=Roboto+Condensed:ital,wght@0,400;0,700;1,400&display=swap" rel="stylesheet">
<style>
  :root{
    --backdrop:#1f221e;
    --paper:#ffffff;
    --forest:#2e5a43;
    --forest-deep:#1d3b2e;
    --forest-band:#3e6a4f;
    --mint:#bfe3cd;
    --mint-pale:#e3f3e9;
    --ink:#2b2b2b;
    --ink-soft:#555;
    --footer-tint:#e9f1f2;
  }
  *{box-sizing:border-box;margin:0;padding:0}
  html,body{width:1200px;height:842px;overflow:hidden}
  body{background:var(--backdrop);font-family:"Roboto Condensed",Arial,sans-serif;color:var(--ink);position:relative}
  .page{position:absolute;top:25px;width:560px;height:792px;background:var(--paper);overflow:hidden;display:flex;flex-direction:column}
  .page--back{left:28px}
  .page--front{left:612px}

  /* shared footer */
  .footer{margin-top:auto;background:var(--footer-tint);display:flex;align-items:center;gap:34px;padding:14px 28px 12px;font-size:8.5px;line-height:1.35;color:var(--ink)}
  .footer__item{display:flex;align-items:center;gap:8px}
  .footer__icon{width:18px;height:18px;background:var(--forest-band);display:flex;align-items:center;justify-content:center;flex:none}
  .footer__bar{height:11px;background:var(--forest-band)}

  /* back side */
  .brand{text-align:center;padding-top:40px;color:var(--forest)}
  .brand__name{font-family:"PT Serif",Georgia,serif;font-size:21px;line-height:1.1}
  .intro{padding:16px 30px 0}
  .section-title{font-family:"PT Serif",Georgia,serif;color:var(--forest);font-size:13px;font-weight:700;margin-bottom:6px}
  .intro__text{font-size:7.4px;line-height:1.72;text-align:justify;color:var(--ink-soft)}
  .intro__text b{color:var(--ink)}
  .founder{display:flex;margin:18px 20px 0 14px;height:258px}
  .founder__panel{width:46%;background:linear-gradient(160deg,#2f5440,#213d30 70%,#2a4a39);color:#e6efe9;padding:38px 14px 14px 18px}
  .founder__title{font-family:"PT Serif",Georgia,serif;color:var(--mint);font-size:15px;margin-bottom:18px}
  .founder__text{font-size:6.9px;line-height:1.75;text-align:justify}
  .founder__text b{color:#fff}
  .founder__photo{flex:1;background:linear-gradient(120deg,#d9dcd6,#eef0ee 45%,#aab7c8 75%,#c9ccc6)}
  .mindset{padding:18px 30px 0}
  .mindset .section-title{font-size:10.5px;font-weight:400}
  .mindset__list{list-style:none;font-size:6.6px;line-height:2.4;color:var(--ink-soft)}
  .mindset__list li::before{content:"•";margin-right:4px}

  /* front side */
  .hero{height:300px;position:relative;background:linear-gradient(100deg,var(--forest-deep) 0%,#26493a 45%,#35604b 75%,#3d6a53 100%);color:#fff;padding:26px 24px 0}
  .hero__photo{position:absolute;inset:0}
  .hero__content{position:relative;width:72%}
  .hero__kicker{font-family:"PT Serif",Georgia,serif;font-size:13px;line-height:1.2}
  .hero__title{font-family:"PT Serif",Georgia,serif;font-weight:700;color:var(--mint);font-size:25px;line-height:1;margin:6px 0 12px}
  .hero__lead{font-family:"PT Serif",Georgia,serif;font-weight:700;font-size:8px;margin-bottom:4px}
  .hero__text{font-size:7px;line-height:1.65;text-align:justify;color:#e8efe9}
  .hero__brand{position:absolute;right:26px;top:120px;text-align:center;font-family:"PT Serif",Georgia,serif;color:var(--mint);font-size:21px;line-height:1.1;width:120px}
  .services{margin:-20px 26px 0;position:relative;background:#fff;border:1px solid #cfd8d2}
  .services__title{background:var(--mint);text-align:center;font-family:"PT Serif",Georgia,serif;font-weight:700;font-size:9.5px;padding:6px 0;color:var(--forest-deep)}
  .striped{background:repeating-linear-gradient(180deg,#fff 0 9px,var(--mint-pale) 9px 18px)}
  .row{display:grid;grid-template-columns:1fr 1fr;gap:12px;padding:4px 10px}
  .col-head{font-family:"PT Serif",Georgia,serif;font-weight:700;font-size:6.6px;line-height:1.25;margin-bottom:2px}
  .list{list-style:none;font-size:6.3px;line-height:9px}
  .list li::before{content:"•";margin-right:4px}
  .band-head{text-align:center;font-family:"PT Serif",Georgia,serif;font-weight:700;font-size:8px;padding:3px 0 0}
  .note{font-size:6.3px;padding:3px 10px;border-top:1px solid #cfd8d2}
  .benefits{border-top:1px solid #cfd8d2;padding:5px 10px 8px}
  .benefits__head{font-family:"PT Serif",Georgia,serif;font-weight:700;font-size:7.6px;margin-bottom:4px}
  .benefits__grid{display:grid;grid-template-columns:1.2fr 1fr 1fr;gap:10px}
  .benefits__grid .list li{margin-bottom:2px}
  .page--front .footer{padding:16px 28px 14px}
</style>
</head>
<body>

<section class="page page--back">
  <header class="brand">
    <div class="brand__name">Corvana Summit Partners</div>
  </header>

  <article class="intro">
    <h2 class="section-title">Our Reasons for Being</h2>
    <p class="intro__text">Today's increasingly competitive environment for middle market <b>Private Equity Funds, Family Offices,</b> and Investment Banks, has left little time for those entities to focus on their marketing strategies, tactics, and execution. At best, a Business Development executive is forced to take on a <b>Marketing</b> role as a part-time, almost side job, taking valuable time away from their in-person deal origination responsibilities. At worst, a GP whose primary focus is on deal evaluation and execution, is forced to give up hours of their time trying to perform tasks in which they are not trained or updated in 21st Century marketing tactics. Marketing goes beyond Business Development but should work with it in an integrated manner to ensure a seamless connection between funds and their three primary target markets: Investors, Private Company Owners, and Deal Sources. <b>Corvana Summit Partners</b> was created to bring <b>Fractional Marketing Services</b> to <b>Private Equity Funds</b> and <b>Family Offices</b> and the <b>Intermediaries</b> and <b>Counselors</b> who serve them. For years, the <b>Fractional Marketing Services</b> concept has been leveraged in Private Equity, but only for <b>Portfolio Companies,</b> with little <b>Corporate Marketing</b> attention given to the funds themselves. Finally, <b>Private Equity Funds,</b> Family Offices, and Investment Banks are realizing they are too busy competing to win the next deal and enhancing Portco equity value to be able to focus on a Marketing and Lead Generation system that is dynamic and ever-changing. At <b>Corvana Summit Partners,</b> we believe that roughly 1/3 of the skills required to be a successful B2B financial services marketer 10-years from now haven't even been identified yet. Why not leave the execution of your critical marketing function to a firm that lives and breathes <b>Private Equity, Family Office,</b> and <b>Investment Bank Marketing</b> full-time? Contact us immediately for a <b>no obligation</b> discussion at <b>1.555.210.4830 or DanielM@CorvanaSummit.com.</b></p>
  </article>

  <article class="founder">
    <div class="founder__panel">
      <h2 class="founder__title">PRINCIPAL &amp; FOUNDER</h2>
      <p class="founder__text">Daniel Mercer has over 25 years of <b>Private Equity</b> experience, 17 of which have been spent as Chief Marketing Officer (CMO) for middle market <b>Private Equity</b> funds. As a past <b>General Partner,</b> his knowledge of <b>Private Equity</b> marketing, business development, fundraising, principal investing, and portfolio-company enhancement, positions him unlike any other in the middle market: <b>"A Marketer with an Investor's Mindset."</b> Daniel has experience in buyouts, non-control/mezzanine, growth equity, ABL, and venture capital asset classes. Unlike agency experienced marketers who operate without firsthand <b>Private Equity</b> empathy, <b>Corvana Summit Partners</b> brings firsthand PE experience and knowledge of what GPs must accomplish with their marketing efforts to satisfy their three primary target markets: investors, Company Owners, and Deal Sources.</p>
    </div>
    <div class="founder__photo" role="img" aria-label="Portrait photo of the founder seated at his office desk"></div>
  </article>

  <article class="mindset">
    <h2 class="section-title">A Marketer With An Investor's Mindset</h2>
    <ul class="mindset__list">
      <li>17-Years as Private Equity Chief Marketing Officer—one of the industry's first</li>
      <li>25-Years total Private Equity experience, including Marketing, Business Development, Fundraising &amp; Principal Investing</li>
      <li>40-Years total Sales and Marketing experience, including Corporate and Global Strategy Consulting</li>
      <li>Experienced in most asset classes, including buyouts, Growth Equity, Mezzanine, ABL and Venture</li>
      <li>More deal, business development, and marketing experience than any Analyst or Associate, typically assigned to these roles</li>
      <li>Arguably, the most experienced middle market Private Equity marketer in the U.S.</li>
    </ul>
  </article>

  <footer class="footer">
    <div class="footer__item">
      <span class="footer__icon"><svg width="9" height="11" viewBox="0 0 9 11"><path d="M4.5 0.5a3.6 3.6 0 0 0-3.6 3.6c0 2.6 3.6 6.4 3.6 6.4s3.6-3.8 3.6-6.4A3.6 3.6 0 0 0 4.5.5z" fill="none" stroke="#fff"/><circle cx="4.5" cy="4.1" r="1.2" fill="#fff"/></svg></span>
      <span>Corvana Summit, LLC, 18 Alder Lane, Suite 204,<br>Fairhaven, CT 06120 USA, 555.210.4830</span>
    </div>
    <div class="footer__item">
      <span class="footer__icon"><svg width="11" height="8" viewBox="0 0 11 8"><rect x=".5" y=".5" width="10" height="7" fill="none" stroke="#fff"/><path d="M.5.5l5 4 5-4" fill="none" stroke="#fff"/></svg></span>
      <span>DanielM@CorvanaSummit.com<br>www.CorvanaSummit.com</span>
    </div>
    <div class="footer__item">
      <span class="footer__icon"><svg width="10" height="10" viewBox="0 0 10 10"><path d="M2 .8l1.6 2.2-1 1c.6 1.3 1.5 2.2 2.7 2.8l1-1L8.6 7.3 7.8 9C4 8.6 1.2 5.8.8 2z" fill="#fff"/></svg></span>
      <span>+44 1632 960410<br>+44 1632 960420</span>
    </div>
  </footer>
  <div class="footer__bar"></div>
</section>

<section class="page page--front">
  <header class="hero">
    <div class="hero__photo" role="img" aria-label="Dark green toned photo of a hand stacking coins"></div>
    <div class="hero__content">
      <p class="hero__kicker">Fractional Marketing Services<br>for Private Equity Funds,</p>
      <h1 class="hero__title">FAMILY OFFICES &amp;<br>INVESTMENT BANKS</h1>
      <p class="hero__lead">Fractional Marketing Services: The Alternative to a Full-Time Marketing Staff</p>
      <p class="hero__text">Hiring a full-time corporate marketing staff, or even a single marketing employee, can be an expensive proposition. <b>Corvana Summit Partners</b> provides <b>Part-Time Marketing</b> Services to middle market clients, which allow them to receive best-in-class corporate marketing at a fraction of the cost of a full-time Analyst or Associate, or even an entry-level Marketing Coordinator. <b>Fractional Marketing Services</b> have been used for years for <b>Private Equity</b> portfolio companies, but only recently have they been made available to <b>Private Equity Funds</b> themselves, <b>Family Offices,</b> and <b>Investment Banks.</b> When selecting a <b>Fractional Marketing Services</b> resource, prospective clients should ensure their <b>Fractional Chief Marketing Officer (CMO)</b> has broad firsthand <b>Private Equity</b> and <b>Banking</b> experience in the areas of Marketing, Business Development, Fundraising, and Principal Investing, which can be leveraged to quickly create differentiated marketing strategies and tactics, along with 21st Century tools to increase lead generation, deal flow, and stakeholder satisfaction.</p>
    </div>
    <div class="hero__brand">Corvana Summit Partners</div>
  </header>

  <section class="services">
    <h2 class="services__title">FRACTIONAL MARKETING SERVICES</h2>
    <div class="striped">
      <div class="row">
        <div>
          <p class="col-head">MONTHLY RETAINED MARKETING SERVICES<br>UP TO 20-HOURS/MONTH<br>STRATEGY, MANAGEMENT &amp; EXECUTION</p>
          <ul class="list">
            <li>Press Release Drafting &amp; Distribution</li>
            <li>Email Campaigns &amp; Drip Marketing / Lead Nurturing</li>
            <li>Digital Marketing &amp; Advertising</li>
            <li>Content Development &amp; Collateral Management</li>
            <li>Website Analysis, Updates &amp; Remarketing</li>
            <li>SEO &amp; SEM</li>
            <li>Dashboard &amp; KPIs</li>
            <li>Vendor Tool Selection &amp; Implementation</li>
            <li>List Management</li>
            <li>Go-to-Market Strategy</li>
            <li>Professional Network Enhancement &amp; Lead Gen</li>
            <li>Other Social Media</li>
            <li>Offline Activity Management</li>
          </ul>
        </div>
        <div>
          <p class="col-head">MARKETING AUDIT &amp; PLANNING SERVICES<br>UP TO 20-HOURS/MONTH<br>STRATEGY, MANAGEMENT &amp; EXECUTION</p>
          <ul class="list">
            <li>Website &amp; Traffic Analysis</li>
            <li>SEO &amp; SEM</li>
            <li>Social Media (e.g., professional networks, etc.)</li>
            <li>Email &amp; Other Digital</li>
            <li>Press Releases</li>
            <li>Collaterals</li>
            <li>Content Management / CMS</li>
            <li>Generative A.I. Tools</li>
            <li>Advertising (if applicable)—all channels</li>
            <li>Full Funnel Evaluation</li>
            <li>Biz Dev &amp; Marketing Integration</li>
            <li>CRM &amp; Data Integrity</li>
            <li>Creative Assessment</li>
          </ul>
        </div>
      </div>
      <p class="band-head">SPECIAL PROJECTS</p>
      <div class="row">
        <ul class="list">
          <li>Branding &amp; Rebranding</li>
          <li>Website Overhaul</li>
          <li>Corporate Identity</li>
          <li>Data Cleansing</li>
          <li>Video Production &amp; Management</li>
        </ul>
        <ul class="list">
          <li>CRM Selection, Design &amp; Transition</li>
          <li>Customer Intelligence Studies</li>
          <li>Marketing Brainstorming &amp; Facilitation</li>
          <li>Marketing Resource Evaluation</li>
          <li>Boards of Directors</li>
        </ul>
      </div>
      <p class="band-head">NEW FUND LAUNCH SERVICES</p>
      <div class="row">
        <ul class="list">
          <li>For Inaugural &amp; Follow-on Funds</li>
          <li>6 &amp; 12-Month Projects</li>
          <li>Limited Availability</li>
          <li>Fees based on fund size, number, stage &amp; complexity</li>
        </ul>
        <ul class="list">
          <li>Inaugural &amp; Follow-on Funds (includes all Fractional Marketing Services above)</li>
          <li>Plus: Website creation or overhaul</li>
          <li>Plus: CRM design &amp; implementation</li>
          <li>Plus: Corporate identity work</li>
          <li>Plus: Social media &amp; digital launch</li>
          <li>Plus: Marketing Audit for follow-on funds</li>
          <li>Plus: Business development and GTM strategy</li>
          <li>6 &amp; 12-Month Projects</li>
        </ul>
      </div>
    </div>
    <p class="note">New Fund Launch Services can commence before or during fundraising</p>
    <div class="benefits">
      <p class="benefits__head">WITH CORVANA SUMMIT PARTNERS FRACTIONAL MARKETING SERVICES, YOU CAN:</p>
      <div class="benefits__grid">
        <ul class="list">
          <li>Receive Best-in-Class Marketing strategies &amp; tactics for a fraction of the cost of an Analyst</li>
          <li>Leverage the experience of a 17+ year middle market Private Equity Chief Marketing Officer</li>
        </ul>
        <ul class="list">
          <li>No benefits or payroll taxes</li>
          <li>No need to stay knowledgeable on marketing and lead generation tactics, which change daily</li>
        </ul>
        <ul class="list">
          <li>100% remote, with onsite work from time-to-time and at your discretion</li>
          <li>Receive LP-friendly reports to prove your differentiation and ensure their satisfaction</li>
        </ul>
      </div>
    </div>
  </section>

  <footer class="footer">
    <div class="footer__item">
      <span class="footer__icon"><svg width="9" height="11" viewBox="0 0 9 11"><path d="M4.5 0.5a3.6 3.6 0 0 0-3.6 3.6c0 2.6 3.6 6.4 3.6 6.4s3.6-3.8 3.6-6.4A3.6 3.6 0 0 0 4.5.5z" fill="none" stroke="#fff"/><circle cx="4.5" cy="4.1" r="1.2" fill="#fff"/></svg></span>
      <span>Corvana Summit, LLC, 18 Alder Lane, Suite 204,<br>Fairhaven, CT 06120 USA, 555.210.4830</span>
    </div>
    <div class="footer__item">
      <span class="footer__icon"><svg width="11" height="8" viewBox="0 0 11 8"><rect x=".5" y=".5" width="10" height="7" fill="none" stroke="#fff"/><path d="M.5.5l5 4 5-4" fill="none" stroke="#fff"/></svg></span>
      <span>DanielM@CorvanaSummit.com<br>www.CorvanaSummit.com</span>
    </div>
    <div class="footer__item">
      <span class="footer__icon"><svg width="10" height="10" viewBox="0 0 10 10"><path d="M2 .8l1.6 2.2-1 1c.6 1.3 1.5 2.2 2.7 2.8l1-1L8.6 7.3 7.8 9C4 8.6 1.2 5.8.8 2z" fill="#fff"/></svg></span>
      <span>+44 1632 960410<br>+44 1632 960420</span>
    </div>
  </footer>
  <div class="footer__bar"></div>
</section>

</body>
</html>
```